Letterhead for New Orthopaedic Surgery Practice

My husband and I are starting our own practice named RB Spine & Vitality Center. We would like to create a nice simple but high class letterhead that doesn't use too much solid color ink when printing. I like the colors dark blue, gold, yellow. Open to other suggestions. We will need to list him and I both on the top of the letterhead. Here is the important information:
Lucinda Perrow, M.D. - Hand and Upper Extremity Surgery
Abena Quist, M.D. - Hip & Knee Replacement/General Orthopaedic Surgery
Location: 18735 North Harlow Pkwy
Lakeview Springs, FL 33490
Phone: 954-218-4650
Fax: 954-582-1346
Email: info@myrbspine.com

The only thing is that the phone and fax numbers will change once we get into our space. I just want to get the design started. I am including several documents which are my previous practice letterhead, my current procedure room letterhead, and our new Logo. The other letterheads are just for examples but please think outside of the box! We would love to see some great designs.

Colors
0054AA
0677BA
7BADD7
CADEEF
E8F1F8
0094D4
00A9DD
6FCCEA
C7EBF8
E9F6FB

Requirements
Must have
• class, elegance, luxury

```html
<!DOCTYPE html>
<html lang="en">
<head>
<meta charset="utf-8">
<title>RB Spine &amp; Vitality Center — Letterhead</title>
<link href="https://fonts.googleapis.com/css2?family=Source+Sans+3:wght@400;600;700&display=swap" rel="stylesheet">
<style>
  :root {
    --navy: #2b3d8c;
    --cyan: #19a9dd;
    --ink: #4a4a4a;
    --ink-dark: #3a3a3a;
    --paper: #ffffff;
    --sign-tone: #e6e8ef;
  }
  * { box-sizing: border-box; margin: 0; padding: 0; }
  html, body { width: 964px; height: 1200px; overflow: hidden; background: var(--paper); }
  body { font-family: "Source Sans 3", "Myriad Pro", sans-serif; color: var(--ink); position: relative; }

  .brand { position: absolute; left: 87px; top: 104px; display: flex; align-items: center; gap: 12px; }
  .brand-mark { width: 18px; height: 18px; border-radius: 50%; background: var(--navy); flex: none; }
  .brand-name { font-size: 24px; font-weight: 700; color: var(--navy); line-height: 1.15; width: 210px; }

  .physicians { position: absolute; right: 291px; top: 81px; text-align: right; }
  .physician-name { font-size: 20px; font-weight: 700; color: var(--navy); line-height: 26px; }
  .physician-specialty { font-size: 15px; color: var(--cyan); line-height: 18px; }
  .physician + .physician { margin-top: 14px; }
  .physician + .physician .physician-name { margin-bottom: 2px; }

  .header-rule { position: absolute; left: 686px; top: 79px; width: 1px; height: 130px; background: var(--ink-dark); }

  .contact { position: absolute; left: 701px; top: 81px; font-size: 15px; color: var(--ink); line-height: 19.5px; font-style: normal; }
  .contact-address { margin-bottom: 4px; }
  .contact-line { display: flex; align-items: center; gap: 12px; }
  .contact-line svg { width: 13px; height: 13px; fill: var(--navy); flex: none; }

  .letter-date { position: absolute; left: 93px; top: 344px; font-size: 17.5px; line-height: 23px; font-weight: 600; color: var(--ink); }
  .recipient { position: absolute; left: 93px; top: 414px; font-size: 17.5px; font-weight: 600; color: var(--ink); line-height: 23.3px; }

  .letter-body { position: absolute; left: 91px; top: 548px; width: 779px; font-size: 15.5px; line-height: 23.3px; color: var(--ink); text-align: justify; hyphens: auto; }
  .letter-body p + p { margin-top: 23.3px; }

  .signature { position: absolute; left: 691px; top: 1023px; width: 158px; height: 60px; background: linear-gradient(90deg, var(--sign-tone), #f3f4f8); border-radius: 4px; }
  .signatory-title { position: absolute; left: 732px; top: 1084px; font-size: 16px; line-height: 20px; color: var(--ink); letter-spacing: 0.2px; }
</style>
</head>
<body>
  <header>
    <div class="brand">
      <span class="brand-mark"></span>
      <span class="brand-name">RB Spine &amp; Vitality Center</span>
    </div>

    <div class="physicians">
      <div class="physician">
        <div class="physician-name">Lucinda Perrow, M.D.</div>
        <div class="physician-specialty">Hand and Upper Extremity Surgery</div>
      </div>
      <div class="physician">
        <div class="physician-name">Abena Quist, M.D.</div>
        <div class="physician-specialty">Hip &amp; Knee Replacement</div>
        <div class="physician-specialty">General Orthopaedic Surgery</div>
      </div>
    </div>

    <div class="header-rule"></div>

    <address class="contact">
      <div class="contact-address">18735 North Harlow Pkwy<br>Lakeview Springs, FL 33490</div>
      <div class="contact-line">
        <svg viewBox="0 0 12 12"><path d="M2.5 0.5 L4.5 2.6 L3.4 4 Q4.6 6.8 8 8.6 L9.4 7.5 L11.5 9.5 L10 11.5 Q4.5 11 0.5 2 Z"/></svg>
        <span>954-218-4650</span>
      </div>
      <div class="contact-line">
        <svg viewBox="0 0 12 12"><rect x="3" y="0.5" width="6" height="3"/><rect x="0.5" y="4" width="11" height="5" rx="1"/><rect x="3" y="8" width="6" height="3.5" fill="#fff" stroke="#2b3d8c" stroke-width="1"/></svg>
        <span>954-582-1346</span>
      </div>
      <div class="contact-line">
        <svg viewBox="0 0 12 12"><rect x="0.5" y="2" width="11" height="8"/><path d="M0.5 2 L6 6.5 L11.5 2" fill="none" stroke="#fff" stroke-width="1"/></svg>
        <span>info@myrbspine.com</span>
      </div>
      <div class="contact-line">
        <svg viewBox="0 0 12 12"><circle cx="6" cy="6" r="5.5"/><path d="M6 0.5 V11.5 M0.5 6 H11.5 M2 3 Q6 5 10 3 M2 9 Q6 7 10 9" fill="none" stroke="#fff" stroke-width="0.8"/></svg>
        <span>www.myrbspine.com</span>
      </div>
    </address>
  </header>

  <main>
    <p class="letter-date">Cartagena de Indias, Ocober 12,2015</p>

    <div class="recipient">
      Sr.<br>
      MARCO SALCEDO<br>
      Web Master<br>
      City
    </div>

    <div class="letter-body">
      <p>Contrary to popular belief, Lorem Ipsum is not simply random text. It has roots in a piece of classical Latin literature from 45 BC, making it over 2000 years old. Daniel Hartwell, a Latin professor at Alder Ridge College in Virginia, looked up one of the more obscure Latin words, consectetur, from a Lorem Ipsum passage, and going through the cites of the word in classical literature,</p>
      <p>discovered the undoubtable source. Lorem Ipsum comes from sections 1.10.32 and 1.10.33 of "de Finibus Bonorum et Malorum" (The Extremes of Good and Evil) by Lucius Maren, written in 45 BC. This book is a treatise on the theory of ethics, very popular during the Renaissance. The first line of Lorem Ipsum, "Lorem ipsum dolor sit amet..", comes from a line in section 1.10.32.</p>
      <p>The standard chunk of Lorem Ipsum used since the 1500s is reproduced below for those interested. Sections 1.10.32 and 1.10.33 from "de Finibus Bonorum et Malorum" by Lucius Maren are also reproduced in their exact original form, accompanied by English versions from the 1914 translation by H. Tolland.</p>
      <p>There are many variations of passages of Lorem Ipsum available, but the majority have suffered alteration in some form, by injected humour, or randomised words which don't look even slightly believable. If you are going to use a passage of Lorem Ipsum, you need to be sure there isn't anything embarrassing hidden in the middle of text. All the Lorem Ipsum generators o</p>
    </div>

    <div class="signature" role="img" aria-label="Handwritten signature of the founder"></div>
    <p class="signatory-title">CEO/ FOUNDER</p>
  </main>
</body>
</html>
```